Web Application Graphic Design Project

We need a design for an online literacy application. The target audience are 9-12 year old children and the application will teach them literacy skills, like essay writing. It is a web-based application called Brivolen and the software developers now need a graphic design to implement into the code - no coding required, just design of the layout.
Wireframes are attached to give an overview of what the functionalities are - it runs in any ordinary web-browser (indicated in the wireframes as well). The application consists of a static background (workspace) onto which individual boxes are added as the student progresses through the tasks. A task panel on the left hand side allows the user to select a task, upon which a popup window will slide open on the right where they enter content. This content is then displayed on the workspace in the background in a box (which can be moved around to organise, seen in frame 3 ). Additional icons on left and right lead to new tasks.
Updates
The wireframe mockup of the application has been updated - please ignore the previous one, which has now been deleted. This is the final version to work from.
Reason: Would like to give more time to allow for a design that meets the young children target audience and for more creative ways for icons and colour schemes.
Reason: We are waiting for some further submissions to come through.
Target Market(s)
9-12 year old school children, so the design should be appealing to both boys and girls.
Industry/Entity Type
Graphic Design
Look and feel
Each slider illustrates characteristics of the customer's brand and the style your logo design should communicate.

```html
<!DOCTYPE html>
<html lang="en">
<head>
<meta charset="utf-8">
<title>Brivolen – Essay Writing</title>
<link href="https://fonts.googleapis.com/css2?family=Sanchez&family=Open+Sans:wght@400;600&display=swap" rel="stylesheet">
<style>
:root{
  --page:#ebecec;
  --frame-top:#e4e4e4;
  --frame-bottom:#bcbcbc;
  --frame-edge:#a9a9a9;
  --rail:#f1f1f1;
  --workspace:#ffffff;
  --panel:#ececec;
  --panel-edge:#c6c6c6;
  --ink:#3f3f3f;
  --ink-soft:#5a5a5a;
  --ink-faint:#9a9a9a;
  --icon:#6b6b6b;
  --green:#7fae1d;
  --brand:#9c2a5a;
  --cancel:#e0616a;
  --home:#8aa83a;
}
*{box-sizing:border-box;margin:0;padding:0}
html,body{width:1144px;height:1200px;overflow:hidden}
body{background:var(--page);font-family:"Sanchez",Georgia,serif;color:var(--ink);position:relative}
.app-frame{position:absolute;left:142px;top:56px;width:862px;height:1091px;border:1px solid var(--frame-edge);border-radius:6px;overflow:hidden;background:var(--workspace);box-shadow:0 1px 3px rgba(0,0,0,.12)}
.toolbar{position:absolute;left:0;top:0;width:100%;height:111px;background:linear-gradient(var(--frame-top),var(--frame-bottom));border-bottom:1px solid var(--frame-edge)}
.brand{position:absolute;left:33px;top:20px;font-size:22px;line-height:30px;letter-spacing:.5px;color:var(--brand)}
.copyright{position:absolute;left:0;width:100%;top:45px;line-height:14px;text-align:center;font-size:12.5px;letter-spacing:.8px;color:var(--ink-soft);padding-left:10px}
.nav-btn{position:absolute;top:62px;width:27px;height:27px;border-radius:50%;background:linear-gradient(#fafafa,#d8d8d8);border:1px solid #b4b4b4;display:flex;align-items:center;justify-content:center}
.address-bar{position:absolute;left:191px;top:63px;width:482px;height:27px;background:#fff;border:1px solid #b9b9b9;border-radius:3px;box-shadow:inset 0 1px 2px rgba(0,0,0,.12)}
.address-bar .drop{position:absolute;left:9px;top:6px;font-size:9px;color:var(--icon);font-family:"Open Sans",sans-serif}
.address-bar svg{position:absolute;right:8px;top:7px}
.search{position:absolute;left:696px;top:63px;width:132px;height:27px;background:#fff;border:1px solid #b9b9b9;border-radius:3px;font-family:"Open Sans",sans-serif;font-size:11px;color:var(--ink-faint);padding:6px 0 0 25px}
.search svg{position:absolute;left:8px;top:8px}
.rail{position:absolute;top:111px;bottom:30px;background:var(--rail)}
.rail-left{left:0;width:58px}
.rail-right{right:0;width:73px}
.footer{position:absolute;left:0;bottom:0;width:100%;height:30px;background:linear-gradient(#cfcfcf,#b9b9b9);border-top:1px solid var(--frame-edge)}
.tool{position:absolute;text-align:center;font-size:11.5px;line-height:12px;color:var(--ink)}
.tool-box{width:35px;height:31px;margin:0 auto 2px;border:1px solid #bdbdbd;border-radius:3px;background:linear-gradient(#fff,#e6e6e6);display:flex;align-items:center;justify-content:center}
.side-item{position:absolute;width:73px;text-align:center;font-size:11.5px;line-height:10px;color:var(--ink)}
.side-item svg{display:block;margin:0 auto 3px}
.task-panel{position:absolute;left:69px;top:122px;width:172px;height:272px;background:var(--panel);border:1px solid var(--panel-edge);border-radius:3px}
.level{position:absolute;top:8px;text-align:center;font-size:7px;line-height:8px;color:var(--ink-soft)}
.level svg{display:block;margin:0 auto 6px}
.ticks{position:absolute;left:112px;top:17px}
.panel-title{position:absolute;left:9px;top:51px;width:155px;font-weight:400;font-size:17.5px;line-height:20px;padding-top:7px;color:var(--ink);white-space:nowrap;border-top:1px solid #dcdcdc}
.menu{list-style:none;position:absolute;left:0;top:0;font-size:11.5px;line-height:14px;color:var(--ink-soft)}
.menu li{position:absolute;white-space:nowrap}
.popup{position:absolute;left:251px;top:215px;width:172px;height:311px;background:var(--panel);border:1px solid var(--panel-edge);border-radius:3px}
.popup::before{content:"";position:absolute;left:-7px;top:11px;width:12px;height:12px;background:var(--panel);border-left:1px solid var(--panel-edge);border-bottom:1px solid var(--panel-edge);transform:rotate(45deg)}
.popup h2{position:absolute;left:10px;top:5px;font-weight:400;font-size:14.5px;line-height:18px;color:var(--ink)}
.popup p{position:absolute;left:11px;top:32px;width:150px;font-size:9.2px;line-height:12.1px;text-align:justify;color:var(--ink)}
.answer{position:absolute;left:11px;top:199px;width:150px;height:64px;background:#fff;border:1px solid #c9c9c9;border-radius:4px;font-size:8.3px;line-height:11.5px;color:var(--ink-faint);padding:13px 24px 0 25px}
.enter-btn{position:absolute;left:51px;top:275px;width:68px;height:25px;border:1px solid #bcbcbc;border-radius:4px;background:linear-gradient(#fff,#e4e4e4);font-size:13.5px;color:var(--ink);text-align:center;line-height:23px}
</style>
</head>
<body>
<div class="app-frame">
  <header class="toolbar">
    <div class="brand">BRIVOLEN</div>
    <div class="copyright">Brivolen.com.au Copyright 2012</div>
    <div class="nav-btn" style="left:28px"><svg width="10" height="10" viewBox="0 0 10 10"><path d="M6.5 1.5 3 5l3.5 3.5" fill="none" stroke="#444" stroke-width="2"/></svg></div>
    <div class="nav-btn" style="left:62px"><svg width="10" height="10" viewBox="0 0 10 10"><path d="M3.5 1.5 7 5 3.5 8.5" fill="none" stroke="#444" stroke-width="2"/></svg></div>
    <div class="nav-btn" style="left:98px"><svg width="10" height="10" viewBox="0 0 10 10"><path d="M2 2l6 6M8 2 2 8" stroke="var(--cancel)" stroke-width="2.2"/></svg></div>
    <div class="nav-btn" style="left:133px"><svg width="16" height="14" viewBox="0 0 16 14"><path d="M8 1 1 7h2v6h4V9h2v4h4V7h2z" fill="var(--home)"/></svg></div>
    <div class="address-bar"><span class="drop">▼</span><svg width="13" height="11" viewBox="0 0 13 11"><path d="M1 6l4 4 7-9" fill="none" stroke="#666" stroke-width="2"/></svg></div>
    <div class="search"><svg width="11" height="11" viewBox="0 0 11 11"><circle cx="4.5" cy="4.5" r="3.3" fill="none" stroke="#777" stroke-width="1.6"/><path d="M7 7l3 3" stroke="#777" stroke-width="1.8"/></svg>Search</div>
  </header>

  <aside class="rail rail-left"></aside>
  <aside class="rail rail-right"></aside>

  <div class="tool" style="left:11px;top:122px;width:37px">
    <div class="tool-box"><svg width="14" height="14" viewBox="0 0 14 14"><path d="M2 12l1-3 7-7 2 2-7 7z" fill="#555"/></svg></div>Lesson
  </div>
  <div class="tool" style="left:4px;top:182px;width:51px">
    <div class="tool-box"><svg width="20" height="14" viewBox="0 0 20 14"><path d="M10 3C7 1 4 1 2 2v10c2-1 5-1 8 1 3-2 6-2 8-1V2c-2-1-5-1-8 1zM10 3v10" fill="none" stroke="#555" stroke-width="1.1"/></svg></div>Activities
  </div>

  <div class="side-item" style="right:0;top:123px"><svg width="20" height="24" viewBox="0 0 20 24"><circle cx="10" cy="7" r="5.5" fill="var(--icon)"/><path d="M1 24c0-7 4-10 9-10s9 3 9 10z" fill="var(--icon)"/></svg>My<br>Name</div>
  <div class="side-item" style="right:0;top:182px"><svg width="22" height="21" viewBox="0 0 22 21"><path d="M11 0l3.2 7 7.5.7-5.7 5 1.7 7.5L11 16.3 4.3 20.2 6 12.7.3 7.7 7.8 7z" fill="var(--icon)"/></svg>Preference</div>
  <div class="side-item" style="right:0;top:228px"><svg width="20" height="23" viewBox="0 0 20 23"><path d="M6 1h12v21H2V5z" fill="#fff" stroke="#555" stroke-width="1.3"/><path d="M6 1v4H2" fill="none" stroke="#555" stroke-width="1.3"/></svg>Samples</div>
  <div class="side-item" style="right:0;top:279px"><svg width="26" height="26" viewBox="0 0 26 26"><rect x="0" y="0" width="26" height="26" rx="2" fill="var(--icon)"/><rect x="5" y="2" width="16" height="9" fill="#fff"/><rect x="6" y="16" width="14" height="10" fill="#fff"/><rect x="12" y="19" width="3" height="5" fill="var(--icon)"/></svg>Save</div>
  <div class="side-item" style="right:0;top:335px"><svg width="36" height="30" viewBox="0 0 36 30"><g fill="var(--icon)"><circle cx="12" cy="11" r="8"/><circle cx="26" cy="21" r="6"/><rect x="10" y="0" width="4" height="22"/><rect x="1" y="9" width="22" height="4"/><rect x="10" y="0" width="4" height="22" transform="rotate(45 12 11)"/><rect x="10" y="0" width="4" height="22" transform="rotate(-45 12 11)"/><rect x="24.5" y="13" width="3" height="16"/><rect x="18" y="19.5" width="16" height="3"/><rect x="24.5" y="13" width="3" height="16" transform="rotate(45 26 21)"/><rect x="24.5" y="13" width="3" height="16" transform="rotate(-45 26 21)"/></g><circle cx="12" cy="11" r="3.5" fill="#f1f1f1"/><circle cx="26" cy="21" r="2.5" fill="#f1f1f1"/></svg>Settings</div>
  <div class="side-item" style="right:0;top:392px"><svg width="26" height="26" viewBox="0 0 26 26"><path d="M8 5a10 10 0 1 0 10 0" fill="none" stroke="#555" stroke-width="3"/><path d="M13 1v11" stroke="#555" stroke-width="3"/></svg>Exit</div>

  <section class="task-panel">
    <div class="level" style="left:5px;width:34px"><svg width="22" height="22" viewBox="0 0 22 22"><text x="11" y="20" text-anchor="middle" font-family="Sanchez,serif" font-size="24" fill="var(--icon)">B</text></svg>Newbie</div>
    <div class="level" style="left:40px;width:40px"><svg width="24" height="22" viewBox="0 0 24 22"><path d="M12 1 1 12h6v9h10v-9h6z" fill="var(--icon)"/></svg>Developer</div>
    <div class="level" style="left:78px;width:28px"><svg width="22" height="22" viewBox="0 0 22 21"><path d="M11 0l3.2 7 7.5.7-5.7 5 1.7 7.5L11 16.3 4.3 20.2 6 12.7.3 7.7 7.8 7z" fill="var(--icon)"/></svg>Star</div>
    <svg class="ticks" width="50" height="12" viewBox="0 0 50 12"><path d="M1 6l4 4 8-9" fill="none" stroke="var(--green)" stroke-width="2.2"/><path d="M19 6l4 4 8-9" fill="none" stroke="var(--green)" stroke-width="2.2"/><path d="M37 6l4 4 8-9" fill="none" stroke="#444" stroke-width="2.2"/></svg>
    <h1 class="panel-title">ESSAY WRITING</h1>
    <ul class="menu">
      <li style="left:9px;top:83px">Overview</li>
      <li style="left:19px;top:100px">The Question</li>
      <li style="left:30px;top:118px">Teacher - Set Q</li>
      <li style="left:30px;top:134px">Your own Q</li>
      <li style="left:30px;top:151px">Pick a Q</li>
      <li style="left:19px;top:172px">Decoding the Q</li>
      <li style="left:19px;top:189px">Your Ideas</li>
      <li style="left:19px;top:206px">Structure</li>
      <li style="left:19px;top:223px">Writing</li>
      <li style="left:19px;top:240px">Review</li>
    </ul>
  </section>

  <section class="popup">
    <h2>Teacher-Set Question</h2>
    <p>If your teacher has given you a question or topic for this essay, then you can enter it below. Then we can work on decoding it into specific key words that you will need to recognize from the question that will allow you to answer it in the best way. If you don't understand any words in the question, use the Dictionary (in the reference section to the right) to check for the meaning of the word.</p>
    <div class="answer">Enter the question your teacher has given you here...</div>
    <div class="enter-btn">Enter</div>
  </section>

  <footer class="footer"></footer>
</div>
</body>
</html>
```